Solo Law Practice Website Design

I am starting a solo law practice that will specialize in criminal defense and family law.

I have a rudimentary understanding of Wordpress as used through the hostmerry web services. The winning design would be compatible with this system so that I can modify content on my own.

I have supplied the written content and the components that I am looking for at the domain name: dorianvaskelaw.example.

I would like to take that content and work it into a website that looks more professional and inviting. The two most important goals of the website are ease of navigation and rich content for search engine spiders (for example, integrating articles into pages rather than linking to a word document).

The winning design should be turnkey for me to upload immediately.
Updates

Reason: I will be traveling.

Target Market(s)

Individuals looking for legal services.

Industry/Entity Type

Defense

Requirements
Must have
• My picture should appear at least once in the site.

The design should allow a space for me to post blog or legal updates. Additionally, there should be functionality for me to add additional articles to the site.
Nice to have
• Appropriate pictures for a legal website to break-up text on pages.

Simple flash features that won't significantly slow loading times.

Widgets that drive traffic to a contact page or function.

```html
<!DOCTYPE html>
<html lang="en">
<head>
<meta charset="utf-8">
<title>Law Offices of Dorian Vaske PLLC</title>
<link href="https://fonts.googleapis.com/css2?family=Cabin:wght@400;500;600;700&family=Open+Sans:wght@300;400;600;700&display=swap" rel="stylesheet">
<style>
:root{
  --brown-dark:#2e1c0b;
  --brown-panel:#3a2714;
  --brown-nav:#3a2916;
  --heading:#2f2418;
  --text:#7b7b7b;
  --text-dark:#3a3a3a;
  --cream:#f3efe9;
  --white:#ffffff;
  --footer:#d9d9d9;
  --link:#3b6fb6;
}
*{margin:0;padding:0;box-sizing:border-box}
html,body{width:801px;height:1200px;overflow:hidden}
body{position:relative;background:linear-gradient(#fff 430px,#fff 900px,#ececec 1157px);font-family:'Open Sans',sans-serif;color:var(--text)}
.abs{position:absolute}
.topbar{left:0;top:0;width:801px;height:29px;background:var(--brown-dark)}
.social{right:80px;top:9px;display:flex;gap:3px}
.social span{width:14px;height:14px;border-radius:3px;background:#5f7fae;display:block}
.masthead{left:0;top:29px;width:801px;height:367px;background:linear-gradient(90deg,#d9d2c8,#f2eee8 20%,#f6f3ef 50%,#f2eee8 80%,#d9d2c8)}
.brand-mark{left:80px;top:37px;width:94px;height:94px;border-radius:50%;background:#3a2512;border:3px solid #b68c52}
.brand-name{left:180px;top:70px;font-family:'Cabin',sans-serif;font-size:19px;line-height:19px;color:#3a2714;letter-spacing:-.3px}
.contact-info{right:79px;top:50px;text-align:right;font-size:8.6px;line-height:10.8px;color:#2f2418;text-transform:uppercase}
.hero{left:72px;top:137px;width:657px;height:259px;background:var(--white);box-shadow:0 0 8px rgba(0,0,0,.15)}
.hero-title{left:109px;top:205px;font-family:'Cabin',sans-serif;font-weight:700;font-size:12.5px;color:#2f2418}
.hero-text{left:109px;top:234px;width:230px;font-family:'Cabin',sans-serif;font-size:10.5px;line-height:18.8px;color:#2f2418;text-transform:uppercase}
.btn-dark{background:linear-gradient(#4a3420,#2a1a0b);color:#fff;font-family:'Cabin',sans-serif;font-weight:700;font-size:8px;display:flex;align-items:center;justify-content:center;border-radius:2px;box-shadow:0 1px 3px rgba(0,0,0,.4)}
.hero-btn{left:106px;top:321px;width:82px;height:21px}
.hero-art{left:400px;top:151px;width:303px;height:241px;background:radial-gradient(ellipse at 50% 55%,#a8743f,#6b4220 45%,#fff 72%)}
.arrow{top:242px;width:26px;height:52px;background:#fff;box-shadow:0 0 4px rgba(0,0,0,.25)}
.arrow.left{left:72px;border-radius:0 26px 26px 0}
.arrow.right{left:703px;border-radius:26px 0 0 26px}
.arrow svg{position:absolute;top:16px;left:6px}
.nav{left:0;top:396px;width:801px;height:30px;background:linear-gradient(#4a3520,var(--brown-nav));}
.nav a{position:absolute;top:10px;font-family:'Cabin',sans-serif;font-size:8.4px;color:#fff;text-decoration:none;white-space:nowrap}
.page-title{left:73px;top:429px;font-family:'Cabin',sans-serif;font-weight:600;font-size:16.5px;color:var(--heading)}
.lead{left:73px;top:463px;font-size:9px;color:var(--text-dark)}
.portrait{left:74px;top:485px;width:159px;height:144px;background:linear-gradient(135deg,#5a3a1e,#2a1a10 60%,#473020);border:1px solid #222}
.prose{font-size:8.4px;line-height:16px;font-weight:300;color:var(--text)}
.prose b{font-family:'Cabin',sans-serif;font-weight:700;font-size:9.3px;color:var(--heading)}
.about{left:238px;top:484px;width:278px}
.attorney-name{left:73px;top:634px;font-family:'Cabin',sans-serif;font-weight:700;font-size:12.3px;color:var(--heading)}
.general{left:74px;top:652px;width:445px}
.areas{left:73px;top:737px;font-size:9px;font-weight:600;color:var(--text-dark)}
.thumb{top:764px;width:138px;height:80px;border:2px solid #2b1c10}
.thumb.criminal{left:74px;background:linear-gradient(#6a5444,#8b7565)}
.thumb.experience{left:226px;background:linear-gradient(#3e2816,#6a4b30)}
.thumb.family{left:379px;background:radial-gradient(ellipse at 50% 60%,#8b5a2e,#fff 70%)}
.col-title{top:851px;font-family:'Cabin',sans-serif;font-weight:600;font-size:11.5px;color:var(--heading)}
.col-text{top:871px;width:128px;font-size:7.3px;line-height:10.6px;color:var(--text-dark);text-align:justify}
.col-btn{top:1005px;width:57px;height:15px;font-size:7px}
.contact-note{left:73px;top:1054px;width:450px}
.share-label{left:73px;top:1103px;font-family:'Cabin',sans-serif;font-weight:700;font-size:9px;color:var(--heading)}
.share{top:1124px;height:12px;font-size:7px;display:flex;align-items:center;padding:0 4px;border-radius:2px}
.share.fb{left:74px;width:37px;background:#4c66a4;color:#fff;font-weight:700}
.share.post{left:118px;width:36px;background:#eef3f8;border:1px solid #c8d2dc;color:#333}
.share.count{left:157px;width:10px;border:1px solid #ccc;font-size:6px;background:#fff;color:#555}
.share-link{top:1123px;font-family:Arial,sans-serif;font-size:8.5px;color:var(--link)}
.footer{left:0;top:1157px;width:801px;height:43px;background:var(--footer)}
.copyright{left:81px;top:1165px;font-size:7.5px;color:#333}
.call-title{left:548px;top:446px;font-family:'Cabin',sans-serif;font-weight:600;font-size:16.5px;color:var(--heading);letter-spacing:.5px}
.call-icon{left:687px;top:431px}
.sidebar{left:541px;top:472px;width:186px;height:558px;background:var(--brown-panel)}
.side-h{left:548px;font-family:'Cabin',sans-serif;font-weight:600;font-size:15px;line-height:17px;color:#fff;letter-spacing:.3px}
.side-label{left:548px;font-size:8.6px;color:#e9e2d8}
.field{left:548px;height:15px;width:173px;background:#fff;border:1px solid #cfc8bf}
.select{left:548px;top:624px;width:110px;height:14px;background:#fff;font-size:8px;color:#222;padding-left:2px;line-height:13px}
.select i{position:absolute;right:2px;top:2px;width:9px;height:9px;border:1px solid #999;background:#eee}
.textarea{left:548px;top:673px;width:145px;height:88px;background:#fff;border:1px solid #cfc8bf}
.pill{left:549px;width:52px;height:17px;border-radius:9px;background:linear-gradient(#fff,#ddd);color:#222;font-size:8.4px;display:flex;align-items:center;justify-content:center}
.dots{left:552px;width:151px;border-top:2px dotted #8a7a66}
.side-small{left:548px;top:850px;width:175px;font-size:7px;line-height:13px;color:#8e8170}
.input-text{font-size:7.6px;color:#222;padding-left:3px;line-height:13px}
.go{left:705px;top:977px;width:17px;height:14px;background:#fff;border:1px solid #999;font-size:6.5px;color:#222;display:flex;align-items:center;justify-content:center}
</style>
</head>
<body>
<div class="abs topbar"></div>
<div class="abs social" aria-label="Social profiles"><span></span><span></span><span></span></div>

<header>
  <div class="abs masthead"></div>
  <div class="abs brand-mark"></div>
  <div class="abs brand-name">Law Offices of<br>Dorian Vaske PLLC</div>
  <address class="abs contact-info" style="font-style:normal">
    Dorian Vaske<br>Attorney-at-Law<br><span style="display:block;margin-top:2px">PO Box 418202</span>St. Paul, MN 55100<br><span style="display:block;margin-top:2px">(612) 555-0148</span><span style="display:block;margin-top:2px">dorian@dorianvaskelaw.example</span>www.dorianvaskelaw.example
  </address>

  <section class="abs hero"></section>
  <div class="abs hero-art" role="img" aria-label="Wooden gavel resting on a block engraved with the word Family"></div>
  <h2 class="abs hero-title">FAMILY LAW</h2>
  <p class="abs hero-text">I am prepared to handle your family law concerns. I can guide you through the process of child custody matters, divorce, wills and nuptial agreements</p>
  <div class="abs btn-dark hero-btn">READ MORE</div>
  <div class="abs arrow left"><svg width="12" height="20" viewBox="0 0 12 20"><path d="M10 2 L3 10 L10 18" fill="none" stroke="#2b1c10" stroke-width="3"/></svg></div>
  <div class="abs arrow right"><svg width="12" height="20" viewBox="0 0 12 20"><path d="M2 2 L9 10 L2 18" fill="none" stroke="#2b1c10" stroke-width="3"/></svg></div>
</header>

<nav class="abs nav">
  <a style="left:86px">HOME</a><a style="left:125px">CONTACT ME</a><a style="left:190px">CRIMINAL LAW</a><a style="left:261px">FAMILY LAW</a><a style="left:321px">WILL DRAFTING</a><a style="left:395px">ATTORNEY PROFILE</a><a style="left:482px">FEES</a><a style="left:515px">LEGAL UPDATES</a><a style="left:590px">ONLINE RESOURCES</a><a style="left:680px">ARTICLES</a>
</nav>

<main>
  <h1 class="abs page-title">Specializing in Criminal Defense and Family Law</h1>
  <p class="abs lead">Delivering legal services in the greater Twin Cities area.</p>
  <div class="abs portrait" role="img" aria-label="Portrait of attorney Dorian Vaske in front of law books"></div>
  <div class="abs prose about">
    <p><b>About Me.</b> My practice is focused on accomplishing your goals through results-oriented work at a discount price. For your convenience, I handle legal matters throughout the Twin Cities, including Hennepin, Ramsey, Anoka, and Washington counties. I understand that legal issues can appear complicated, and that is why I take a hands-on approach to guiding you through your legal needs.</p>
    <p style="margin-top:2px"><b>Personal Attention.</b> I control the size of my practice so that I am able to devote 100% of my effort to each case. I have no “associates” so I handle every case personally.</p>
  </div>
  <h2 class="abs attorney-name">DORIAN VASKE, ATTORNEY</h2>
  <div class="abs prose general">
    <p><b>General Practice.</b> I am available to provide your defense if you are accused of a felony or misdemeanor. Additionally, I can work with you on family matters such as divorce, child custody, wills, and nuptial agreements.</p>
    <p><b>In our first consultation,</b> I will take time to listen to your individual situation. I will explain the legal issues, and the risks involved in each course of action we may pursue so that you can make informed decisions about how to proceed.</p>
  </div>
  <h3 class="abs areas">My areas of specialization are as follows:</h3>

  <div class="abs thumb criminal" role="img" aria-label="Hands held in handcuffs"></div>
  <div class="abs thumb experience" role="img" aria-label="Open law book on a desk before a bookcase"></div>
  <div class="abs thumb family" role="img" aria-label="Gavel on a block marked Family"></div>

  <h3 class="abs col-title" style="left:74px">CRIMINAL LAW</h3>
  <p class="abs col-text" style="left:74px">Convictions carry serious consequences and can often have a negative financial impact as well as putting your freedom in jeopardy. I know how to work on your behalf because I used to work at the Ridgeline County Attorney’s Office and appeared on the prosecution’s behalf for more than 600 cases. I will prepare your defense, negotiate plea bargains if desired, or take the case to trial.</p>
  <h3 class="abs col-title" style="left:226px">EXPERIENCE MATTERS</h3>
  <p class="abs col-text" style="left:226px">Every case is different. You can take comfort knowing that I have appeared in court on a wide variety of cases including assault, drug possession and distribution, DWI, disorderly conduct, theft, burglary, domestic assault, check forgery, violations or orders for protection, firearms violations and DWI test refusals. I am also prepared to handle your probation violation or expungement.</p>
  <h3 class="abs col-title" style="left:379px">FAMILY LAW</h3>
  <p class="abs col-text" style="left:379px">I am prepared to handle your family law concerns. I can guide you through the process of child custody matters, divorce, wills and nuptial agreements to ensure that you receive a fair and equitable result on these sensitive matters.</p>

  <div class="abs btn-dark col-btn" style="left:74px">READ MORE</div>
  <div class="abs btn-dark col-btn" style="left:230px">READ MORE</div>
  <div class="abs btn-dark col-btn" style="left:379px">READ MORE</div>

  <p class="abs prose contact-note"><b>Contact me.</b> To discuss how the Law Offices of Dorian Vaske can help you, call us at (612) 555-0148 to arrange for you free consultation.</p>

  <h4 class="abs share-label">Share this:</h4>
  <div class="abs share fb">Share</div>
  <div class="abs share post">Post</div>
  <div class="abs share count">0</div>
  <span class="abs share-link" style="left:185px">✉ Email</span>
  <span class="abs share-link" style="left:225px">⎙ Print</span>
</main>

<aside>
  <h2 class="abs call-title">CALL DIRECT</h2>
  <svg class="abs call-icon" width="29" height="29" viewBox="0 0 29 29" aria-label="Phone">
    <rect x="1" y="1" width="27" height="22" rx="3" fill="none" stroke="#2f2418" stroke-width="2"/>
    <path d="M6 22 L4 28 L12 22 Z" fill="#2f2418"/>
    <path d="M9 6 c-2 2 0 7 4 10 c3 2 6 3 7 1 l-2-3 l-2 1 c-2-1-4-3-4-5 l1-2 z" fill="#2f2418"/>
  </svg>
  <div class="abs sidebar"></div>
  <h2 class="abs side-h" style="top:484px">CONTACT FORM</h2>
  <label class="abs side-label" style="top:507px">Name(required)</label>
  <div class="abs field" style="top:522px"></div>
  <label class="abs side-label" style="top:542px">Email</label>
  <div class="abs field" style="top:556px"></div>
  <label class="abs side-label" style="top:576px">Phone</label>
  <div class="abs field" style="top:590px"></div>
  <label class="abs side-label" style="top:609px">Preferred Contact Method</label>
  <div class="abs select">Phone<i></i></div>
  <label class="abs side-label" style="top:643px;width:170px;line-height:12px">Please briefly describe your legal issue (required)</label>
  <div class="abs textarea"></div>
  <div class="abs pill" style="top:768px">Subscribe</div>
  <div class="abs dots" style="top:798px"></div>
  <h2 class="abs side-h" style="top:808px">SUBSCRIBE TO RECEIVE<br>LEGAL UPDATES</h2>
  <p class="abs side-small">Enter your email address to receive notifications of legal updates by e-mail</p>
  <div class="abs field input-text" style="top:880px;width:174px">Email Address</div>
  <div class="abs pill" style="top:903px">Subscribe</div>
  <div class="abs dots" style="top:938px"></div>
  <h2 class="abs side-h" style="top:952px">SEARCH</h2>
  <div class="abs field input-text" style="top:977px;width:155px">SEARCH HERE...</div>
  <div class="abs go">GO</div>
</aside>

<footer>
  <div class="abs footer"></div>
  <p class="abs copyright">© 2012 Law Offices of Dorian Vaske PLLC</p>
</footer>
</body>
</html>
```